Backup Software Tri-fold Brochure Project

We need a great looking and informative brochure to describe our new Backup Software offering. The brochures are to be used in retail and small business environments given to clients interested in protecting their computer from data loss.
The brochure should include attractive imagery that conveys a sense of Trust and Security to the prospective client.
The copy is provided as an attachment to this project. We'd like our Bright Deskpoint product logo to be printed on the back cover. The logo is attached to this project.
The finished tri-fold brochure will be submitted to Plumcopy for printing as an 8.5" x 11" tri-fold brochure. Their design instructions are online http://plumcopy-example.com/custom-brochures.aspx.
The finished product should be Adobe Illustrator CS3 (*.ai) with a PDF Proof.
Target Market(s)
Retail and Small Business customers
Industry/Entity Type
Software
Designer to choose colors to be used in the design.

```html
<!DOCTYPE html>
<html lang="en">
<head>
<meta charset="utf-8">
<title>Bright Deskpoint Offsite Backup – Tri-fold Brochure</title>
<link rel="stylesheet" href="https://fonts.googleapis.com/css2?family=Lato:wght@300;400;700&family=Oswald:wght@500;600;700&family=Anton&display=swap">
<style>
  :root{
    --blue:#1b62a8;
    --blue-deep:#1858a0;
    --green:#5db546;
    --green-dark:#4aa037;
    --ink:#222;
    --grey-bg:#e9e9e9;
    --canvas:#6f7072;
  }
  *{box-sizing:border-box;margin:0;padding:0}
  html,body{width:1200px;height:1200px;overflow:hidden;background:var(--canvas)}
  body{position:relative;font-family:"Lato",sans-serif;color:var(--ink)}
  .sheet{position:absolute;left:220px;width:900px;height:700px;background:#fff;transform-origin:0 0;transform:scale(.844);box-shadow:0 6px 14px rgba(0,0,0,.35);overflow:hidden}
  .sheet--outside{top:6px}
  .sheet--inside{top:603px}
  .panel{position:absolute;top:0;height:700px;overflow:hidden}
  .shape{position:absolute;left:0;top:0}
  .photo{position:absolute}
  .heading{font-family:"Oswald",sans-serif;font-weight:600;font-size:15px;letter-spacing:.2px;color:var(--blue);text-transform:uppercase}
  .body-copy{font-size:12.4px;line-height:15.3px;text-align:justify;font-weight:400}
  .body-copy p+p{margin-top:15px}
  .abs{position:absolute}

  /* outside sheet */
  .how{left:0;width:306px;background:linear-gradient(90deg,#fff 55%,#f1f1f1)}
  .know{left:306px;width:288px}
  .cover{left:594px;width:306px;background:#ededed}
  .know .heading{color:#fff}
  .stats{list-style:none;color:#fff}
  .stats li{position:relative;padding-left:13px;font-size:12px;font-weight:700;margin-bottom:16.5px}
  .stats li::before{content:"";position:absolute;left:0;top:5px;width:4px;height:4px;border-radius:50%;background:#fff}
  .notes{color:#fff;font-size:6px;line-height:17.5px}
  .brand{display:flex;align-items:center;gap:8px;font-family:"Lato",sans-serif;font-weight:700;font-size:22px;color:var(--blue)}
  .brand i{display:block;width:18px;height:18px;background:var(--green)}
  .copyright{font-size:8.5px;color:#333;text-align:center}
  .cover-title{font-family:"Oswald",sans-serif;font-weight:700;text-align:center;line-height:1.1}
  .cover-title .l1{font-size:30px;color:#2a2a2a}
  .cover-title .l2{font-size:29px;color:var(--green)}
  .cover-title .risk{font-family:"Anton",sans-serif;font-weight:400;font-size:104px;color:var(--blue);line-height:1;letter-spacing:1px}

  /* inside sheet */
  .life{left:0;width:308px}
  .todo{left:308px;width:292px}
  .need{left:600px;width:300px}
  .todo .heading{color:var(--green)}
  .todo-copy{font-size:12.6px;line-height:16px}
  .todo-copy strong{font-weight:700}
  .todo-copy p+p{margin-top:8px}
  .options{color:#fff}
  .options .heading{color:#fff}
  .options ul{list-style:none}
  .options li{position:relative;padding-left:22px;font-size:12.6px;line-height:16px;text-align:justify;margin-top:9px}
  .options li::before{content:"";position:absolute;left:2px;top:5px;width:7px;height:7px;border-radius:50%;background:#fff}
</style>
</head>
<body>

<!-- Outside: how it works / did you know / front cover -->
<section class="sheet sheet--outside">
  <div class="panel how">
    <div class="photo" role="img" aria-label="Photo of a technician at a laptop in a server room" style="left:0;top:390px;width:306px;height:310px;background:linear-gradient(180deg,rgba(255,255,255,1) 0%,rgba(200,210,222,.6) 20%,#4d6580 55%,#1f2c3d 100%)"></div>
    <h2 class="heading abs" style="left:33px;top:21px">How it works</h2>
    <div class="body-copy abs" style="left:33px;top:52px;width:254px">
      <p>Our technology is designed to take advantage of the powerful imaging technology embedded in Northgate Paneos. Deep within the core of the OS is an imaging engine that can create a point-in-time backup of the Paneos Operating System, device drivers, programs and system state. The backup can be used later to recover the system back to this point-in-time.</p>
      <p>Backups created by our Imaging technology can even be used to restore Paneos to dissimilar hardware. This is a quick way to migrate to a new computer without having to reinstall everything from scratch.</p>
      <p>Our technology stores backups as Northgate "Virtual Hard Disk" (VHD). These VHD files can be directly mounted from the Paneos Disk Manager. This is a great way to browse the contents of your Image Backup and restore individual files and folders.</p>
    </div>
  </div>

  <div class="panel know">
    <div class="photo" role="img" aria-label="Illustration of a network of computers and cloud storage on a glowing grid" style="left:0;top:300px;width:288px;height:290px;background:linear-gradient(180deg,rgba(93,181,70,0) 0%,#6fb95a 25%,#cfd6d2 60%,#fff 100%)"></div>
    <svg class="shape" width="288" height="700" viewBox="0 0 288 700" aria-hidden="true">
      <polygon points="0,0 288,0 288,300 0,300" fill="var(--green)"/>
      <polygon points="0,300 288,300 288,497 0,420" fill="var(--green-dark)" opacity=".55"/>
      <line x1="0" y1="420" x2="288" y2="497" stroke="var(--blue)" stroke-width="3"/>
    </svg>
    <h2 class="heading abs" style="left:20px;top:21px">Did you know?</h2>
    <p class="abs" style="left:20px;top:50px;color:#fff;font-size:12.4px;font-weight:300">Every week (in the US)</p>
    <ul class="stats abs" style="left:20px;top:80px;width:262px">
      <li>140,000 drives crash (1)</li>
      <li>12,000 laptops are lost or stolen (2)</li>
      <li>37,000 Internet Crimes are committed (3)</li>
      <li>Internet criminals steal $25 Million (3)</li>
    </ul>
    <div class="notes abs" style="left:20px;top:209px;width:262px">
      <p>(1) http://www.laptopstudy-example.com/downloads/lost_laptop_study.pdf</p>
      <p>(2) http://research.diskstats-example.com/archive/disk_failures.pdf</p>
      <p>(3) https://www.netcrime-example.org/media/annualreport/2016_Report.pdf</p>
    </div>
    <div class="brand abs" style="left:48px;top:598px"><i></i>Bright Deskpoint</div>
    <p class="copyright abs" style="left:0;top:667px;width:288px">Copyright(c) 2017, Harlow-Net, Inc. All Rights Reserved</p>
  </div>

  <div class="panel cover">
    <svg class="shape" width="306" height="700" viewBox="0 0 306 700" aria-hidden="true">
      <defs>
        <linearGradient id="coverFade" x1="0" y1="0" x2="0" y2="1">
          <stop offset="0" stop-color="#f3f3f3"/><stop offset="1" stop-color="#dcdcdc"/>
        </linearGradient>
      </defs>
      <rect width="306" height="700" fill="url(#coverFade)"/>
    </svg>
    <div class="photo" role="img" aria-label="Photo of a businessman's hands cupped around a glowing padlock shield" style="left:0;top:0;width:306px;height:500px;background:radial-gradient(circle at 50% 48%,#e9eef2 0%,#9ea5ab 30%,#6d7378 70%,#55595d 100%);clip-path:polygon(0 0,100% 0,100% 420px,0 497px)"></div>
    <svg class="shape" width="306" height="700" viewBox="0 0 306 700" aria-hidden="true">
      <line x1="0" y1="497" x2="306" y2="420" stroke="var(--green)" stroke-width="4"/>
    </svg>
    <div class="cover-title abs" style="left:0;top:500px;width:306px">
      <div class="l1">Your entire</div>
      <div class="l2">Digital Life is at</div>
      <div class="risk">RISK</div>
    </div>
  </div>
</section>

<!-- Inside: entire digital life / what to do + options / what you need -->
<section class="sheet sheet--inside">
  <div class="panel life">
    <svg class="shape" width="308" height="200" viewBox="0 0 308 200" aria-hidden="true">
      <polygon points="0,0 308,0 308,178 0,118" fill="var(--green)"/>
      <line x1="0" y1="118" x2="308" y2="178" stroke="var(--blue)" stroke-width="3"/>
    </svg>
    <div class="photo" role="img" aria-label="Illustration of a green cloud beside a database stack" style="left:78px;top:14px;width:150px;height:118px;border-radius:40px;background:radial-gradient(circle at 45% 45%,#7ccb62,#4c9b38 70%,rgba(76,155,56,0) 100%)"></div>
    <h2 class="heading abs" style="left:33px;top:180px">Your entire digital life is at risk</h2>
    <div class="body-copy abs" style="left:33px;top:212px;width:247px">
      <p>Your computer stores everything you've ever created. Everything you've written, every email you've sent, every list you've made, every picture you've taken or movie you've made, all music you've created, your proposals, your spreadsheets, your presentations, your word files, your artwork, programs you've written, anything you've dictated, and much more... All your digital life is stored on your computer and is at risk of loss without backup.</p>
      <p>And your computer stores a copy of all your personal information. Your passwords, your online banking, your PINs, your credit cards and all your health and shopping records. This makes it a juicy target for hackers. Every day your digital life is exposed to computer Viruses, Malware and spammers all trying to break in. If they succeed the damage could be incalculable.</p>
      <p>If hackers destroy your information or a simple hard drive failure happens, restoring your programs will cost you days of effort and potentially hundreds of dollars. But your files could be unrecoverable. This means the loss of everything you've ever created.</p>
      <p style="text-align:left">The only protection is a great backup.</p>
    </div>
  </div>

  <div class="panel todo">
    <div class="photo" role="img" aria-label="Photo of an engineer holding a laptop in a data center, touching floating screens" style="left:0;top:0;width:292px;height:190px;background:linear-gradient(180deg,#5f7a95 0%,#9fb3c6 55%,#fff 100%)"></div>
    <svg class="shape" width="292" height="700" viewBox="0 0 292 700" aria-hidden="true">
      <polygon points="0,452 292,372 292,700 0,700" fill="var(--blue-deep)"/>
      <line x1="0" y1="452" x2="292" y2="372" stroke="var(--green)" stroke-width="6"/>
    </svg>
    <h2 class="heading abs" style="left:33px;top:221px">What to do</h2>
    <div class="todo-copy abs" style="left:33px;top:253px;width:250px">
      <p><strong>Call us to schedule a day to bring in your computer</strong></p>
      <p>OR</p>
      <p>Once a month we do "Image Backup Saturday". Drop off your computer in the morning and pick it up a few hours later. Call for a copy of our schedule.</p>
    </div>
    <div class="options abs" style="left:34px;top:486px;width:225px">
      <h2 class="heading">Options</h2>
      <p style="font-size:12.6px;font-weight:700;line-height:16px;margin-top:14px">Our Image Backup technology can protect</p>
      <ul>
        <li>Paneos PC's and Laptops running Paneos 7 and above (Paneos 8, 10+)</li>
        <li style="margin-top:16px">Paneos Servers running Paneos 2008 and above (Paneos 2012, 2016+)</li>
      </ul>
    </div>
  </div>

  <div class="panel need">
    <h2 class="heading abs" style="left:42px;top:40px">We have what you need</h2>
    <div class="body-copy abs" style="left:42px;top:72px;width:228px">
      <p>We can create a snapshot of all the programs and files on your computer using our Image Backup technology. We'll give you your backup on an external hard drive which you can store someplace safe. If anything happens, just bring in your computer and your Image Backup and we'll restore your computer back to the point when the snapshot was taken.</p>
      <p>Restoring from an Image Backup is like setting your computer back in time. To make sure all your new files are protected, we'll also install Harlow-Net's Bright Deskpoint software to backup your files every night. These backups are stored in Harlow-Net's secure datacenter to protect you from even the most severe data loss scenarios.</p>
      <p>The combination of your Image Backup and your nightly backup will ensure you have complete protection for both your programs and your files. It means complete peace of mind.</p>
    </div>
    <div class="photo" role="img" aria-label="Photo of an adult hand gently holding a baby's hand" style="left:0;top:560px;width:300px;height:140px;background:linear-gradient(180deg,#fff 0%,#e3cbb3 35%,#b98a63 70%,#7f5a3e 100%)"></div>
  </div>
</section>

</body>
</html>
```